Business Card Design Project

Looking for a logo and business card for a Real State Business i will be opening. The name is not choosen yet , but will probably be RTV IMOVEIS.
I was thinking black and silver colors, but am open to nice ideas.
I did add a business card that i liked a lot, am looking for something like that, with logo in black or silver in a black card. The logo i was thinking in the letters RTV as i uploaded or something or little and cute buildings or a house...just ideas, can be any nice logo.
Updates

You guys can add other colors if you want, I like colors very "BRIGHT" and "open", like red, pink, strong colors. almost glow in the dark colors. lol

Designers,

I've increased more 88 dollars in the budget for 1st place cause I will want envelope designs... small and big sizes.

So 1st place is now U$248,00. 

No need to send the envelope designs right now... only the business cards designs.

Thank you.

Industry/Entity Type

Business

Requirements
Must have
• Renata Tavares Vilela

www.RTVimoveis-exemplo.com.br

+554188316402

renata@rtvimoveis-exemplo.com.br

```html
<!DOCTYPE html>
<html lang="pt-BR">
<head>
<meta charset="utf-8">
<title>RTV Imoveis – Cartão de visita</title>
<link rel="stylesheet" href="https://fonts.googleapis.com/css2?family=Didact+Gothic&display=swap">
<style>
  :root {
    --backdrop: #3a3a3a;
    --card: #0b0b0b;
    --ink: #f2f2f2;
    --ink-soft: #d8d8d8;
    --brand-red: #ea3a5c;
    --brand-yellow: #f3d43a;
  }
  * { box-sizing: border-box; margin: 0; padding: 0; }
  html, body {
    width: 1200px;
    height: 652px;
    overflow: hidden;
    background: var(--backdrop);
    font-family: "Didact Gothic", "Helvetica Neue", Arial, sans-serif;
  }
  .sheet {
    width: 1200px;
    height: 652px;
    display: flex;
    align-items: center;
    justify-content: center;
    gap: 48px;
  }
  .card {
    width: 540px;
    height: 310px;
    background: var(--card);
    color: var(--ink);
    position: relative;
    box-shadow: 0 18px 40px rgba(0, 0, 0, 0.45);
  }
  .brand {
    display: flex;
    align-items: center;
    gap: 12px;
  }
  .brand-name {
    font-size: 54px;
    letter-spacing: 4px;
    color: var(--brand-red);
    line-height: 1;
  }
  .brand-square {
    width: 22px;
    height: 22px;
    background: var(--brand-yellow);
  }
  /* front */
  .card--front .brand {
    position: absolute;
    left: 48px;
    top: 128px;
  }
  .holder {
    position: absolute;
    left: 262px;
    top: 96px;
  }
  .holder-name {
    font-size: 21px;
    letter-spacing: 0.5px;
    margin-bottom: 34px;
  }
  .contact-list {
    list-style: none;
    font-size: 14px;
    line-height: 1.45;
    color: var(--ink-soft);
  }
  /* back */
  .card--back {
    display: flex;
    flex-direction: column;
    align-items: center;
    justify-content: center;
    gap: 26px;
  }
  .card--back .brand-name { font-size: 72px; }
  .card--back .brand-square { width: 28px; height: 28px; }
  .website {
    font-size: 13px;
    color: var(--ink-soft);
    letter-spacing: 0.3px;
  }
</style>
</head>
<body>
  <main class="sheet">
    <section class="card card--front" aria-label="Frente do cartão">
      <div class="brand">
        <span class="brand-name">RTV</span>
        <span class="brand-square"></span>
      </div>
      <div class="holder">
        <p class="holder-name">Renata Tavares Vilela</p>
        <ul class="contact-list">
          <li>+554188316402</li>
          <li>renata@rtvimoveis-exemplo.com.br</li>
          <li>www.RTVimoveis-exemplo.com.br</li>
        </ul>
      </div>
    </section>

    <section class="card card--back" aria-label="Verso do cartão">
      <div class="brand">
        <span class="brand-name">RTV</span>
        <span class="brand-square"></span>
      </div>
      <p class="website">www.RTVimoveis-exemplo.com.br</p>
    </section>
  </main>
</body>
</html>
```